We require a banner design for a 53' x 10' trailer for a future development to be displayed on the side of the highway. The development name is 712 35 Commerce Park, logo is attached. This is an industrial future development. Please also include the RLW Group logo and MERO Development logos as well.

Industry/Entity Type

Real Estate / Construction / Developer / Industrial Future Development

Requirements
Must have
• Logos provided

```html
<!DOCTYPE html>
<html lang="en">
<head>
<meta charset="utf-8">
<title>712 35 Commerce Park – Trailer Banner</title>
<link rel="stylesheet" href="https://fonts.googleapis.com/css2?family=Montserrat:wght@400;500;600;700&display=swap">
<style>
  :root {
    --page-bg: #e9ebea;
    --panel-white: #ffffff;
    --ink: #0d0d0d;
    --rule: #c9c9c9;
    --accent-red: #d3272f;
  }
  html, body {
    margin: 0;
    padding: 0;
    width: 1200px;
    height: 1200px;
    overflow: hidden;
    background: var(--page-bg);
  }
  .canvas {
    width: 1200px;
    height: 1200px;
    display: flex;
    align-items: center;
    justify-content: center;
  }
  .trailer-banner {
    display: block;
    width: 1100px;
    height: 400px;
    box-shadow: 0 2px 10px rgba(0,0,0,0.12);
  }
  .brand-number {
    font-family: "Montserrat", sans-serif;
    font-weight: 700;
    fill: var(--ink);
  }
  .brand-sub {
    font-family: "Montserrat", sans-serif;
    font-weight: 400;
    fill: var(--ink);
  }
  .partner-name {
    font-family: "Montserrat", sans-serif;
    font-weight: 600;
    fill: var(--ink);
  }
  .headline {
    font-family: "Montserrat", sans-serif;
    font-weight: 500;
    fill: var(--panel-white);
  }
  .phone-number {
    font-family: "Montserrat", sans-serif;
    font-weight: 500;
    fill: var(--panel-white);
  }
</style>
</head>
<body>
<main class="canvas">
  <svg class="trailer-banner" viewBox="0 0 1100 400" xmlns="http://www.w3.org/2000/svg" aria-label="712 35 Commerce Park trailer banner">
    <rect class="banner-base" x="0" y="0" width="1100" height="400" fill="var(--panel-white)"/>

    <polygon class="message-panel" points="399,23 1083,23 1083,380 502,380" fill="var(--ink)"/>
    <line class="accent-rule" x1="389" y1="23" x2="490" y2="380" stroke="var(--ink)" stroke-width="4"/>

    <g class="development-identity">
      <text class="brand-number" x="345" y="124" font-size="84" text-anchor="end" textLength="270" lengthAdjust="spacingAndGlyphs">712</text>
      <text class="brand-number" x="345" y="214" font-size="84" text-anchor="end" textLength="179" lengthAdjust="spacingAndGlyphs">35</text>
      <text class="brand-sub" x="74" y="256" font-size="26" textLength="274" lengthAdjust="spacingAndGlyphs">COMMERCE PARK</text>
    </g>

    <g class="partner-strip">
      <rect x="74" y="286" width="274" height="54" fill="none" stroke="var(--rule)" stroke-width="1.5"/>
      <line x1="221" y1="286" x2="221" y2="340" stroke="var(--rule)" stroke-width="1.5"/>
      <rect x="86" y="304" width="18" height="18" fill="none" stroke="var(--ink)" stroke-width="1.5"/>
      <text class="partner-name" x="112" y="319" font-size="15">MERO DEV.</text>
      <circle cx="244" cy="313" r="8" fill="var(--accent-red)"/>
      <text class="partner-name" x="260" y="321" font-size="24">RLW</text>
    </g>

    <text class="headline" x="493" y="185" font-size="62" textLength="531" lengthAdjust="spacingAndGlyphs">YOUR TEXT HERE</text>
    <g class="phone-line">
      <circle cx="584" cy="240" r="15" fill="none" stroke="var(--panel-white)" stroke-width="3"/>
      <path d="M578 232 q-2 9 6 15 q4 2 7 0 l-3 -4 q-2 1 -4 -1 q-3 -3 -2 -5 l-2 -4 z" fill="var(--panel-white)"/>
      <text class="phone-number" x="612" y="257" font-size="46" textLength="340" lengthAdjust="spacingAndGlyphs">555-013-2468</text>
    </g>
  </svg>
</main>
</body>
</html>
```